A Billboard Sign - TWO SIGNS

Hi, I’m looking to produce approximately 2.74 m by 2.74 m for a billboard-style display. I have a mock-up of the general look and feel, but I need a more polished, professional design. The sign will be viewed by people driving past, so the messaging must be clear, bold and easily readable at speed.

I also need a second sign sized 1 m by 3 m, following the same branding and visual style as the larger piece.

Requirements
Must have
• It must use the colours I've submitted
Nice to have
• I would like to see some good ideas in the general theme of what I have Mocked up. I don't the same design sent back to me

```html
<!DOCTYPE html>
<html lang="en">
<head>
<meta charset="utf-8">
<title>Brightline Systems – Billboard</title>
<link rel="stylesheet" href="https://fonts.googleapis.com/css2?family=Red+Hat+Display:wght@500;700;800;900&display=swap">
<style>
  :root {
    --orange-deep: #dd7414;
    --orange-light: #f0a43a;
    --gold: #eaa321;
    --navy: #15222a;
    --navy-light: #34454e;
    --white: #f2f2f2;
    --white-shade: #dcdcdc;
    --ink: #17252d;
    --grey-text: #7a7a7a;
    --page: #e6e6e6;
  }
  * { margin: 0; padding: 0; box-sizing: border-box; }
  html, body { width: 1100px; height: 1200px; overflow: hidden; }
  body {
    background: var(--page);
    font-family: "Red Hat Display", Arial, sans-serif;
    position: relative;
  }
  .billboard {
    position: absolute;
    left: 30px; top: 80px;
    width: 1040px; height: 1040px;
    overflow: hidden;
  }
  .billboard-bg { position: absolute; inset: 0; }
  .brand {
    position: absolute; left: 62px; top: 62px;
    display: flex; align-items: center; gap: 52px;
  }
  .brand-mark {
    width: 180px; height: 180px; border-radius: 50%;
    background: var(--ink);
  }
  .brand-name {
    font-weight: 800; font-size: 74px; line-height: 70px;
    letter-spacing: 3px; color: var(--ink); text-transform: uppercase;
  }
  .headline { position: absolute; left: 52px; top: 340px; }
  .headline-accent {
    font-weight: 900; font-size: 86px; line-height: 96px;
    color: var(--gold); letter-spacing: -1px;
  }
  .headline-main {
    font-weight: 800; font-size: 60px; line-height: 68px;
    color: var(--white); letter-spacing: -0.5px;
  }
  .rule {
    position: absolute; left: 54px; top: 690px;
    width: 60px; height: 6px; background: var(--gold);
  }
  .website {
    position: absolute; left: 52px; top: 712px;
    font-size: 31px; font-weight: 700; color: var(--white);
  }
  .website-tld { font-weight: 500; color: var(--gold); }
  .partners-label {
    position: absolute; left: 52px; top: 872px;
    font-weight: 800; font-size: 22px; color: var(--ink);
    transform: rotate(-2.2deg); transform-origin: left center;
    letter-spacing: 0.3px;
  }
  .partners {
    position: absolute; top: 935px; left: 0; width: 1040px;
    display: flex; justify-content: center; align-items: center; gap: 44px;
    padding-left: 40px;
  }
  .partner-name { font-weight: 700; font-size: 38px; color: var(--grey-text); }
  .partner-divider { width: 1px; height: 60px; background: #c9c9c9; }
  .partner { display: flex; align-items: center; gap: 14px; }
  .partner-square { width: 40px; height: 40px; background: var(--grey-text); }
</style>
</head>
<body>
  <main class="billboard">
    <svg class="billboard-bg" width="1040" height="1040" viewBox="0 0 1040 1040" aria-hidden="true">
      <defs>
        <linearGradient id="bandOrange" x1="0" x2="1" y1="0" y2="0">
          <stop offset="0" stop-color="var(--orange-deep)"/>
          <stop offset="0.5" stop-color="var(--orange-light)"/>
          <stop offset="0.8" stop-color="var(--orange-deep)"/>
          <stop offset="1" stop-color="var(--orange-light)"/>
        </linearGradient>
        <radialGradient id="panelNavy" cx="0.55" cy="0.35" r="0.6">
          <stop offset="0" stop-color="var(--navy-light)"/>
          <stop offset="1" stop-color="var(--navy)"/>
        </radialGradient>
        <linearGradient id="footWhite" x1="0" x2="1" y1="0" y2="0">
          <stop offset="0" stop-color="var(--white-shade)"/>
          <stop offset="0.5" stop-color="var(--white)"/>
          <stop offset="1" stop-color="var(--white-shade)"/>
        </linearGradient>
      </defs>
      <rect class="band-top" x="0" y="0" width="1040" height="300" fill="url(#bandOrange)"/>
      <rect class="panel-main" x="0" y="300" width="1040" height="740" fill="url(#panelNavy)"/>
      <path class="panel-foot" d="M0 914 L468 908 L452 880 Q760 868 1040 880 V1040 H0 Z" fill="url(#footWhite)"/>
      <path class="partners-ribbon" d="M0 878 L430 862 L452 896 L470 908 L0 916 Z" fill="var(--gold)"/>
    </svg>

    <header class="brand">
      <div class="brand-mark"></div>
      <div class="brand-name">Brightline<br>Systems</div>
    </header>

    <section class="headline">
      <h1 class="headline-accent">Award Winning</h1>
      <p class="headline-main">Data Analytics<br>Implementation<br>Partner</p>
    </section>

    <div class="rule"></div>
    <p class="website">brightline-systems<span class="website-tld">.com</span></p>

    <p class="partners-label">PROUDLY PARTNERING WITH</p>
    <div class="partners">
      <span class="partner-name">KESTREL</span>
      <span class="partner-divider"></span>
      <span class="partner"><span class="partner-square"></span><span class="partner-name">Veltrix</span></span>
    </div>
  </main>
</body>
</html>
```